Label Design for a New Alcoholized Root Beer

Create a design for a new alcoholized root beer. This is a new product category in the USA growing very rapidly. Root Beer is a popular flavor of Cola, but recently, beer manufacturers have added alcohol to it and have created a new product that has gained traction on the market at a tremendous rate.

Root Beer is vintage product that has been around for a hundred years. Consumers of this product are mostly male between the age of 30 to 45. They purchase this product for its nostalgia and vintage look and taste.

This product will be in a standard 355 mL brown bottle.

It is 5.9% abv.

The name of the product is ''Corvel's Hard Root Beer''.

We have uploaded some pictures of traditional root beers to give you an idea of the feel we want our product to have and also, the bottle the product will be filled in.

Target Market(s)

Consumers are male 30-45, same market as craft beer consumers

Industry/Entity Type

Product

Requirements
Must have
• Design must have a vintage feel to it

```html
<!DOCTYPE html>
<html lang="en">
<head>
<meta charset="utf-8">
<title>Corvel's Hard Root Beer – Label</title>
<link href="https://fonts.googleapis.com/css2?family=Oswald:wght@500;700&family=Roboto:wght@400&display=swap" rel="stylesheet">
<style>
  :root {
    --backdrop-light: #f4f4f4;
    --backdrop-dark: #d6d6d6;
    --glass-brown: #4a2418;
    --label-brown: #3a1d16;
    --ink-cream: #f1ebe5;
    --ornament-tone: #b8a9a2;
    --ornament-shade: #8c7a72;
  }
  * { margin: 0; padding: 0; box-sizing: border-box; }
  html, body { width: 1200px; height: 1200px; overflow: hidden; }
  body {
    background: radial-gradient(circle at 50% 50%, var(--backdrop-light) 35%, var(--backdrop-dark) 100%);
    position: relative;
    color: var(--ink-cream);
  }

  /* Neck print */
  .neck-print {
    position: absolute;
    left: 440px; top: 40px;
    width: 320px; height: 280px;
    background: var(--glass-brown);
    border-radius: 24px;
    text-align: center;
  }
  .neck-ornament {
    width: 150px; height: 54px;
    margin: 30px auto 0;
    background: linear-gradient(180deg, var(--ornament-tone), var(--ornament-shade));
    opacity: .75;
    border-radius: 6px;
  }
  .neck-name {
    font-family: "Oswald", sans-serif;
    font-weight: 500;
    font-size: 34px;
    line-height: 42px;
    letter-spacing: 1px;
    margin-top: 24px;
  }

  /* Main label */
  .main-label {
    position: absolute;
    left: 320px; top: 360px;
    width: 560px; height: 780px;
  }
  .label-frame { position: absolute; inset: 0; }
  .label-content { position: absolute; inset: 0; text-align: center; }

  .crest-ornament {
    position: absolute;
    left: 190px; top: 82px;
    width: 180px; height: 54px;
    background: linear-gradient(180deg, var(--ornament-tone), var(--ornament-shade));
    opacity: .75;
    border-radius: 6px;
  }
  .spec-bar {
    position: absolute;
    left: 95px; top: 152px;
    width: 370px; height: 32px;
    border: 1.5px solid var(--ink-cream);
    border-radius: 4px;
    display: flex; justify-content: space-between; align-items: center;
    padding: 0 14px;
    font-family: "Roboto", sans-serif;
    font-size: 15px;
  }
  .flourish {
    position: absolute;
    width: 110px; height: 28px;
    background: linear-gradient(90deg, var(--ornament-tone), var(--ornament-shade));
    opacity: .7;
    border-radius: 14px;
  }
  .flourish.upper-left { left: 82px; top: 218px; }
  .flourish.upper-right { right: 82px; top: 218px; }
  .flourish.lower-left { left: 78px; top: 478px; }
  .flourish.lower-right { right: 78px; top: 478px; }
  .brand-name {
    position: absolute;
    left: 0; right: 0; top: 268px;
    font-family: "Oswald", sans-serif;
    font-weight: 500;
    font-size: 50px;
    line-height: 62px;
    letter-spacing: 2px;
  }
  .hatch-rule {
    position: absolute;
    left: 120px; top: 535px;
    width: 320px; height: 12px;
    background: repeating-linear-gradient(135deg, var(--ink-cream) 0 2px, transparent 2px 7px);
    opacity: .8;
  }
  .quality-mark {
    position: absolute;
    left: 0; right: 0; top: 566px;
    font-family: "Oswald", sans-serif;
    font-weight: 700;
    line-height: 1;
  }
  .quality-mark .quality-main { display: block; font-size: 50px; }
  .quality-mark .quality-sub { display: block; font-size: 24px; font-weight: 500; letter-spacing: 1px; margin-top: 2px; }
</style>
</head>
<body>

  <section class="neck-print">
    <div class="neck-ornament" role="img" aria-label="Floral filigree ornament"></div>
    <p class="neck-name">CORVEL'S HARD<br>ROOT BEER</p>
  </section>

  <section class="main-label">
    <svg class="label-frame" viewBox="0 0 560 780" width="560" height="780" aria-hidden="true">
      <path d="M60,120 Q280,-20 500,120 L500,140 Q520,140 520,160 L520,640 Q500,640 500,660 L500,690 Q280,800 60,690 L60,660 Q40,660 40,640 L40,160 Q60,160 60,140 Z"
            fill="var(--label-brown)" stroke="var(--ink-cream)" stroke-width="3"/>
      <path transform="translate(280 390) scale(0.93) translate(-280 -390)"
            d="M60,120 Q280,-20 500,120 L500,140 Q520,140 520,160 L520,640 Q500,640 500,660 L500,690 Q280,800 60,690 L60,660 Q40,660 40,640 L40,160 Q60,160 60,140 Z"
            fill="none" stroke="var(--ink-cream)" stroke-width="1.5"/>
    </svg>

    <div class="label-content">
      <div class="crest-ornament" role="img" aria-label="Floral filigree crest"></div>

      <div class="spec-bar"><span>5.9% abv</span><span>355 ML</span></div>

      <div class="flourish upper-left" role="img" aria-label="Scroll flourish"></div>
      <div class="flourish upper-right" role="img" aria-label="Scroll flourish"></div>

      <h1 class="brand-name">CORVEL'S HARD<br>ROOT BEER</h1>

      <div class="flourish lower-left" role="img" aria-label="Scroll flourish"></div>
      <div class="flourish lower-right" role="img" aria-label="Scroll flourish"></div>

      <div class="hatch-rule"></div>

      <p class="quality-mark">
        <span class="quality-main">Awesome</span>
        <span class="quality-sub">QUALITY</span>
      </p>
    </div>
  </section>

</body>
</html>
```